Kelvo Brook Website

Design and implement (fully coded and ready to launch) website for a professional services company - please see the documents attached and send us an email if there are any questions
Target Market(s)
Market to potential clients about the services we offer and be able to reach us for any consulting opportunities
Industry/Entity Type
Professional Service
Coding
Coded - Design and coding required
Number of Pages Required
3 page
Requirements
Must have
- Single page website design that is SEO optimized
Blog Post
Contact US page
Cool images/ logos for the service offering - not fill the website with text/content
Must be professional looking website
Coded website should also look great on different screens - mobile, tablets etc
Nice to have
- Choose easy neutral colors that compliment the logo colors. Having said that don't use every color in the logo for the website design.
Should not have
- Too many colors and several various different fonts

```html
<!DOCTYPE html>
<html lang="en">
<head>
<meta charset="utf-8">
<title>Kelvo Brook LLC</title>
<link href="https://fonts.googleapis.com/css2?family=Poppins:wght@400;500;600;700;800&display=swap" rel="stylesheet">
<style>
:root{
  --orange:#f26a21;
  --navy:#233a8f;
  --blue:#2f55c4;
  --purple:#6a3aa6;
  --magenta:#b2377f;
  --pink-soft:#fbe3e6;
  --ink:#1e1e2a;
  --muted:#6d6f7b;
  --tile:#eeeeef;
  --line:#d9dbe2;
  --white:#ffffff;
}
*{box-sizing:border-box;margin:0;padding:0}
html,body{width:1200px;height:4484px;overflow:hidden}
body{font-family:"Poppins",sans-serif;color:var(--ink);background:var(--white);position:relative}
.section{position:absolute;left:0;width:1200px}
.btn{display:inline-block;border-radius:30px;font-weight:600;font-size:15px;text-transform:uppercase;padding:12px 26px;color:var(--white);background:var(--orange);text-decoration:none}
.btn-outline{background:var(--white);color:var(--navy)}
.art{position:absolute;border-radius:8px}

/* header */
.site-header{top:0;height:88px;background:var(--white);display:flex;align-items:center;padding:0 110px;justify-content:space-between;border-top:4px solid var(--blue)}
.brand{display:flex;align-items:center;gap:10px;font-weight:700;font-size:26px;color:var(--navy)}
.brand-mark{width:18px;height:18px;border-radius:50%;background:var(--orange)}
.nav{display:flex;gap:34px;font-size:15px;font-weight:500;align-items:center}
.nav a{color:var(--ink);text-decoration:none}
.nav a.active{color:var(--orange)}
.nav .btn{padding:10px 30px;font-size:14px;margin-left:30px}

/* hero */
.hero{top:88px;height:640px;background:linear-gradient(120deg,var(--navy) 0%,var(--purple) 50%,var(--magenta) 100%);clip-path:polygon(0 0,100% 0,100% 86%,0 100%)}
.hero h1{position:absolute;left:110px;top:176px;color:var(--white);font-size:50px;font-weight:800}
.hero p{position:absolute;left:110px;top:246px;width:440px;color:var(--white);font-size:15px;font-weight:600;line-height:1.5}
.hero .actions{position:absolute;left:110px;top:320px;display:flex;gap:16px}
.hero .actions .btn{font-size:13px;padding:10px 22px}
.dots{position:absolute;left:110px;top:476px;display:flex;gap:8px}
.dots span{width:12px;height:12px;border-radius:50%;background:var(--white)}
.hero .art{left:600px;top:40px;width:560px;height:500px;background:linear-gradient(135deg,#e9eefc,#b9c6f3 60%,#8fa3e6);opacity:.9}

/* about */
.about{top:760px;height:560px}
.about .art{left:130px;top:120px;width:360px;height:320px;background:linear-gradient(135deg,#e6ecfb,#9fb1ea)}
.about-text{position:absolute;left:600px;top:130px;width:490px}
.about h2{font-size:40px;font-weight:400}
.about h2 b{font-weight:800}
.about .lead{font-size:15px;font-weight:600;line-height:1.55;margin:14px 0 18px}
.about .body{font-size:13px;color:var(--muted);line-height:1.7;margin-bottom:24px}

/* services */
.services{top:1300px;height:800px;background:linear-gradient(180deg,#fdeef0,var(--pink-soft) 60%,#fbe9ec);clip-path:polygon(0 14%,100% 0,100% 100%,0 88%)}
.section-title{text-align:center;font-size:40px;font-weight:400;color:var(--ink)}
.section-title b{font-weight:800}
.services .section-title{margin-top:150px}
.service-row{display:flex;justify-content:center;gap:70px;margin-top:40px}
.service{width:250px;text-align:center}
.service .art{position:relative;display:block;width:210px;height:210px;border-radius:50%;margin:0 auto;background:linear-gradient(135deg,#ffffff,#dfe6fb)}
.service h3{font-size:21px;font-weight:600;margin-top:28px}
.service p{font-size:13px;color:var(--muted);line-height:1.6;margin:12px 0 22px}
.service .btn{font-size:12px;padding:9px 22px}

/* tech */
.tech{top:2100px;height:560px}
.tech .section-title{margin-top:70px;color:var(--ink)}
.tech-grid{display:grid;grid-template-columns:repeat(4,236px);gap:12px;justify-content:center;margin-top:36px}
.tech-tile{height:110px;background:var(--tile);display:flex;align-items:center;justify-content:center;gap:10px;font-weight:600;font-size:20px;color:#3b3f55}
.tech-tile i{width:16px;height:16px;background:#9aa1b8;display:block}
.tech-tile.c2{grid-column:2}

/* blog */
.blog{top:2660px;height:880px;background:linear-gradient(135deg,var(--purple) 0%,var(--navy) 55%,var(--blue) 100%);clip-path:polygon(0 0,100% 16%,100% 88%,0 100%)}
.blog .section-title{margin-top:200px;color:var(--white);font-weight:800}
.blog-row{display:flex;justify-content:center;gap:20px;margin-top:36px}
.post{width:316px;color:var(--white)}
.post .art{position:relative;display:block;height:176px;border-radius:0;background:linear-gradient(135deg,#f2f5fe,#bac8f1)}
.post .cat{font-size:13px;margin:10px 0 8px;display:flex;align-items:center;gap:8px}
.post .cat i{width:12px;height:12px;background:var(--white);display:block;border-radius:2px}
.post .head{display:flex;gap:10px}
.date{width:40px;height:40px;background:var(--orange);font-size:11px;font-weight:700;text-align:center;line-height:1.2;padding-top:6px;flex:none}
.post h4{font-size:15px;font-weight:600;line-height:1.35}
.post p{font-size:13px;line-height:1.55;margin:10px 0;opacity:.9}
.post .more{font-size:13px;font-weight:700;text-decoration:underline}

/* contact */
.contact{top:3540px;height:500px}
.contact-intro{position:absolute;left:110px;top:60px}
.contact-intro .kicker{font-size:20px;font-weight:700}
.contact-intro .name{font-size:20px;margin-top:4px}
.contact-intro .chat{font-size:38px;font-weight:800;color:var(--orange);margin-top:4px}
.contact-intro .art{position:relative;display:block;width:270px;height:130px;margin-top:50px;background:linear-gradient(135deg,#f5f6fa,#e6e8ef)}
.contact-form{position:absolute;left:430px;top:60px;width:660px;display:grid;grid-template-columns:1fr 1fr;gap:20px}
.field{border:1px solid var(--line);height:60px;padding:18px;font-size:13px;color:#8d90a0}
.field.wide{grid-column:1/3;height:130px}
.contact-form .btn{grid-column:1/3;justify-self:start;padding:14px 44px}

/* footer */
.footer{top:4020px;height:464px;background:linear-gradient(120deg,var(--navy),var(--blue));clip-path:polygon(0 12%,100% 0,100% 100%,0 100%);color:var(--white)}
.footer-cols{position:absolute;left:110px;top:110px;width:980px;display:grid;grid-template-columns:290px 170px 240px 1fr;gap:20px}
.footer .brand{color:var(--white);font-size:24px}
.footer .about-line{font-size:13px;line-height:1.6;margin-top:14px}
.footer h5{font-size:17px;font-weight:700;margin-bottom:16px}
.footer ul{list-style:none;font-size:13px;line-height:2.1}
.contact-list li{display:flex;align-items:center;gap:10px;margin-bottom:8px}
.subscribe-input{height:44px;background:var(--white);color:#8d90a0;font-size:13px;padding:12px}
.subscribe-btn{height:44px;background:var(--orange);font-size:13px;font-weight:700;text-align:center;line-height:44px;letter-spacing:1px;margin-top:8px}
.socials{display:flex;gap:12px;margin-top:18px;justify-content:center}
.socials span{width:30px;height:30px;border-radius:50%;background:rgba(255,255,255,.25)}
.socials span.on{background:var(--orange)}
.copyright{position:absolute;left:110px;right:110px;bottom:30px;border-top:1px solid rgba(255,255,255,.3);padding-top:20px;text-align:center;font-size:13px}
</style>
</head>
<body>

<header class="section site-header">
  <div class="brand"><span class="brand-mark"></span>KELVO BROOK</div>
  <nav class="nav">
    <a class="active" href="#">Home</a>
    <a href="#">Our Services</a>
    <a href="#">About Us</a>
    <a href="#">Careers</a>
    <a href="#">Resources</a>
    <a href="#">Contact</a>
    <a class="btn" href="#">Join</a>
  </nav>
</header>

<section class="section hero">
  <h1>KELVO BROOK LLC</h1>
  <p>Kelvo Brook provides end to end services in architecture, design and development of Data Platforms, Analytic workloads, Data Engineering, Cloud Engineering</p>
  <div class="actions"><a class="btn btn-outline" href="#">Know Details</a><a class="btn" href="#">Get Started</a></div>
  <div class="dots"><span></span><span></span><span></span></div>
  <div class="art" role="img" aria-label="Isometric illustration of a team working around data dashboards and charts"></div>
</section>

<section class="section about">
  <div class="art" role="img" aria-label="Illustration of a person presenting analytics on a large screen"></div>
  <div class="about-text">
    <h2><b>ABOUT</b> KELVO BROOK LLC</h2>
    <p class="lead">Kelvo Brook provides end to end services in architecture, design and development of Data Platforms, Analytic workloads, Data Engineering, Cloud Engineering</p>
    <p class="body">Our team partners closely with each client to plan, build and run modern data systems. We focus on clear design, reliable delivery and lasting support so that every platform keeps growing with the business and its people, today and over the years ahead.</p>
    <a class="btn" href="#">Learn More</a>
  </div>
</section>

<section class="section services">
  <h2 class="section-title"><b>OUR</b> SERVICES</h2>
  <div class="service-row">
    <div class="service">
      <span class="art" role="img" aria-label="Illustration of a person beside a large light bulb and blueprint panels"></span>
      <h3>Platform Architecture</h3>
      <p>Kelvo Brook works very closely with clients, product managers to understand the scope of the requirements.</p>
      <a class="btn" href="#">Learn More &#8594;</a>
    </div>
    <div class="service">
      <span class="art" role="img" aria-label="Illustration of engineers building data pipelines"></span>
      <h3>Data Engineering</h3>
      <p>Kelvo Brook employs the latest proven technologies, best practices, industry standards in</p>
      <a class="btn" href="#">Learn More &#8594;</a>
    </div>
    <div class="service">
      <span class="art" role="img" aria-label="Illustration of people working with cloud servers"></span>
      <h3>Cloud Developments</h3>
      <p>There are numerous technology options, tools, cloud services that can be utilized but guiding through</p>
      <a class="btn" href="#">Learn More &#8594;</a>
    </div>
  </div>
</section>

<section class="section tech">
  <h2 class="section-title"><b>OUR TECHNOLOGY</b> EXPERTISE</h2>
  <div class="tech-grid">
    <div class="tech-tile"><i></i>Ringvale</div>
    <div class="tech-tile"><i></i>Embermill</div>
    <div class="tech-tile"><i></i>Quillstream</div>
    <div class="tech-tile"><i></i>Frostlane</div>
    <div class="tech-tile"><i></i>Brookset</div>
    <div class="tech-tile"><i></i>Nimbara</div>
    <div class="tech-tile"><i></i>Relaypost</div>
    <div class="tech-tile"><i></i>Skyvault</div>
    <div class="tech-tile c2"><i></i>Taskwell</div>
    <div class="tech-tile"><i></i>Corecloud</div>
  </div>
</section>

<section class="section blog">
  <h2 class="section-title">KELVO BROOK BLOG</h2>
  <div class="blog-row">
    <article class="post">
      <span class="art" role="img" aria-label="Isometric illustration of a server room"></span>
      <div class="cat"><i></i>Platform Architecture</div>
      <div class="head"><div class="date">05<br>JUN</div><h4>Sed ut perspiciatis unde omnis iste natus error sit volupt</h4></div>
      <p>Lorem ipsum dolor sit amet, consectetur adipi scing elit, sed do eiusmod tempor</p>
      <a class="more">READ MORE &#8594;</a>
    </article>
    <article class="post">
      <span class="art" role="img" aria-label="Illustration of a team reviewing data charts"></span>
      <div class="cat"><i></i>Data Engineering</div>
      <div class="head"><div class="date">05<br>JUN</div><h4>Sed ut perspiciatis unde omnis iste natus error sit volupt</h4></div>
      <p>Lorem ipsum dolor sit amet, consectetur adipi scing elit, sed do eiusmod tempor</p>
      <a class="more">READ MORE &#8594;</a>
    </article>
    <article class="post">
      <span class="art" role="img" aria-label="Illustration of a person working on a cloud dashboard"></span>
      <div class="cat"><i></i>Cloud Developments</div>
      <div class="head"><div class="date">05<br>JUN</div><h4>Sed ut perspiciatis unde omnis iste natus error sit volupt</h4></div>
      <p>Lorem ipsum dolor sit amet, consectetur adipi scing elit, sed do eiusmod tempor</p>
      <a class="more">READ MORE &#8594;</a>
    </article>
  </div>
</section>

<section class="section contact">
  <div class="contact-intro">
    <div class="kicker">Ready to Experience</div>
    <div class="name">Kelvo Brook</div>
    <div class="chat">Let's Chat</div>
    <span class="art" role="img" aria-label="Faint world map backdrop"></span>
  </div>
  <form class="contact-form">
    <div class="field">Name*</div>
    <div class="field">Email Address*</div>
    <div class="field">Phone*</div>
    <div class="field">Subject*</div>
    <div class="field wide">Message*</div>
    <span class="btn">Submit &#8594;</span>
  </form>
</section>

<footer class="section footer">
  <div class="footer-cols">
    <div>
      <div class="brand"><span class="brand-mark"></span>KELVO BROOK</div>
      <p class="about-line">Kelvo Brook provides end to end services in architecture, design and development of Data Platforms, Analytic workloads, Data Engineering, Cloud Engineering</p>
    </div>
    <div>
      <h5>Useful Links</h5>
      <ul><li>Our Services</li><li>About Us</li><li>Careers</li><li>Resources</li><li>Contact</li></ul>
    </div>
    <div>
      <h5>Contact</h5>
      <ul class="contact-list">
        <li><svg width="16" height="16" viewBox="0 0 24 24" fill="#fff"><path d="M6.6 10.8a15 15 0 006.6 6.6l2.2-2.2a1 1 0 011-.25 11.4 11.4 0 003.6.57 1 1 0 011 1V20a1 1 0 01-1 1A17 17 0 013 4a1 1 0 011-1h3.5a1 1 0 011 1c0 1.25.2 2.45.57 3.57a1 1 0 01-.25 1z"/></svg>+00 555 01 000</li>
        <li><svg width="16" height="16" viewBox="0 0 24 24" fill="#fff"><path d="M3 5h18v14H3z M3 5l9 7 9-7" stroke="#233a8f" stroke-width="1.5"/></svg>hello@kelvobrook.com</li>
        <li><svg width="16" height="16" viewBox="0 0 24 24" fill="#fff"><path d="M12 2a7 7 0 00-7 7c0 5 7 13 7 13s7-8 7-13a7 7 0 00-7-7zm0 9.5A2.5 2.5 0 1112 6.5a2.5 2.5 0 010 5z"/></svg>12 Harbor Lane, Westfield</li>
      </ul>
    </div>
    <div>
      <h5>Subscribe</h5>
      <div class="subscribe-input">Email Address</div>
      <div class="subscribe-btn">SUBSCRIBE US</div>
      <div class="socials"><span></span><span></span><span class="on"></span><span></span></div>
    </div>
  </div>
  <div class="copyright">&#169; Copyright 2020 Kelvo Brook LLC. All Rights Reserved.</div>
</footer>

</body>
</html>
```